Music Producer Website

I need a website designed for my music production company. We specialize in finding talented musicians and matching them with music producers all over the United States. A visitor can create a profile and/or upload their music demo and we submit it to thousands of music producers and production companies for review. In many cases, our members will receive multiple signing offers from music producers allowing them to choose the contract that is best for them. "We turn aspiring musicians into SuperStars!"
Please include photos that reflect all genres of music (black artists, white artists, both male and female.) We produce all types of music including rap, R&B, rock, country, and Hip Hop.
When a user creates a profile, they become visible to thousands of record producers who are looking to sign new talent and make them stars.
Somewhere in the top half of the page, please include a small form that the visitor can fill out. The form should look as follows:
Title (large and bold): Contact Us or Submit Music Demo
Fields to include (* = required): First Name*, Last Name*, Age, Zip Code, Email Address*, Daytime Phone, Evening Phone, Comments
Then, there will be a "submit" button to proceed to next step of form. Just below the "submit" button, should be the following verbiage: "After submitting, you will have the opportunity to upload demos of your music (optional) and provide other pertinent information about yourself, band, or group."
Reason: I have not seen a design that I am 100% satisfied with yet. Ideally, rotating header images (GIF or other) with several different music producers in studio (male, female, black, white) would be perfect. Here are some examples of how the header pics could look:
http://media.quillfarrow.net/design_img/402913/550871/550871_7719046_402913_image.jpg
http://media.quillfarrow.net/design_img/402913/550871/550871_7719058_402913_image.jpg
http://media.quillfarrow.net/design_img/402913/550871/550871_7719037_402913_image.jpg
Also, there should be a form on the site (somewhere in upper half of the page) with the following headline:
GET FOUND AND BECOME A STAR! (super large, super-bold font)
Contact Us or Submit Your Music for Review (large font, not as bold as headline)
First Name
Last Name
Age
Zip Code
Email Address
Daytime Phone
Evening Phone
Comments
We are targeting all types of musicians including rock, rap, pop, R&B, country, gospel, etc.
Artists
Designer to choose colors to be used in the design.

```html
<!DOCTYPE html>
<html lang="en">
<head>
<meta charset="utf-8">
<title>Vireo Music Productions</title>
<link href="https://fonts.googleapis.com/css2?family=Lato:wght@300;400;700;900&display=swap" rel="stylesheet">
<style>
:root{
  --ink:#0b0b0b;
  --panel:#141414;
  --gold:#b3a47a;
  --gold-deep:#a8976b;
  --white:#ffffff;
  --muted:#bdbdbd;
  --field-text:#a9a9a9;
  --sand:#e7dfd5;
  --accent-red:#c8432b;
  --line:#5e5a50;
}
*{box-sizing:border-box;margin:0;padding:0}
html,body{width:1200px;height:2261px;overflow:hidden;background:var(--ink)}
body{font-family:'Lato',Arial,sans-serif;color:var(--white);position:relative}
.abs{position:absolute}

/* hero */
.hero{position:absolute;left:0;top:0;width:1200px;height:942px;overflow:hidden}
.hero-photo{position:absolute;inset:0;
  background:
   radial-gradient(ellipse 420px 300px at 330px 260px,#d9d6d0 0%,rgba(160,160,160,.55) 45%,transparent 75%),
   radial-gradient(ellipse 500px 260px at 900px 140px,#9fb4c4 0%,#6d7f8c 40%,transparent 80%),
   radial-gradient(ellipse 700px 300px at 600px 420px,#b89a78 0%,rgba(90,70,55,.7) 50%,transparent 90%),
   linear-gradient(180deg,#6f7780 0%,#3a3530 55%,#151210 100%)}
.hero-arrow{position:absolute;left:1140px;top:278px}

.site-header{position:absolute;left:119px;top:0;width:957px;height:122px;background:#121212}
.brand{position:absolute;left:32px;top:38px;color:var(--gold);font-weight:700;line-height:1}
.brand .brand-name{font-size:36px;letter-spacing:2px;display:block}
.brand .brand-sub{font-size:11px;letter-spacing:2.4px;display:block;margin-top:6px}
.account-link{position:absolute;left:654px;top:25px;font-size:14px;color:var(--white)}
.social{position:absolute;top:21px;width:26px;height:26px;border-radius:50%;background:#5a564d}
.search{position:absolute;left:913px;top:19px;width:30px;height:30px;border-radius:50%;background:var(--gold-deep)}
.main-nav{position:absolute;left:386px;top:64px;display:flex;font-size:15px;font-weight:700}
.main-nav a{color:var(--white);text-decoration:none;padding-top:18px;position:relative}
.main-nav a span{color:var(--gold)}
.main-nav a.active::before{content:"";position:absolute;left:-4px;top:0;width:102px;height:3px;background:var(--gold)}
.nav-about{margin-right:54px}.nav-team{margin-right:54px}.nav-join{margin-right:54px}

.tagline-small{position:absolute;left:688px;top:335px;width:386px;height:42px;background:var(--white);color:var(--ink);font-weight:700;font-size:25px;line-height:42px;padding-left:10px}
.tagline-big{position:absolute;left:672px;top:377px;width:402px;height:90px;background:rgba(20,20,20,.85);font-weight:700;font-size:72px;line-height:88px;text-align:right;padding-right:10px}

/* form panel */
.signup{position:absolute;left:75px;top:537px;width:1061px;height:405px;background:rgba(12,12,12,.82)}
.signup h2{position:absolute;left:46px;top:20px;font-weight:700;line-height:1}
.signup .h-small{font-size:41px;display:block}
.signup .h-big{font-size:70px;color:var(--gold);display:block;margin-top:4px}
.field{position:absolute;background:var(--white);color:var(--field-text);font-size:16px;font-weight:300;padding:6px 0 0 12px}
.req{position:absolute;font-size:12px;color:var(--muted)}
.artist-photo{position:absolute;left:697px;top:9px;width:306px;height:283px;
  background:radial-gradient(ellipse 140px 150px at 150px 160px,#8c8c8c 0%,#3b3b3b 60%,#141414 100%)}
.submit{position:absolute;left:697px;top:299px;width:306px;height:44px;background:var(--gold-deep);color:var(--white);font-weight:900;font-size:30px;text-align:center;line-height:44px;letter-spacing:1px}
.form-note{position:absolute;left:0;top:362px;width:1061px;text-align:center;font-size:13px;color:var(--gold)}

/* welcome */
.welcome{position:absolute;left:0;top:942px;width:1200px;height:377px;
  background:
   radial-gradient(ellipse 260px 200px at 700px 230px,#a7835a 0%,rgba(90,62,38,.8) 45%,transparent 80%),
   linear-gradient(90deg,#2a2017 0%,#4d3a28 45%,#3b2b1d 75%,#1b1510 100%)}
.welcome h2{position:absolute;left:160px;top:98px;font-size:72px;font-weight:700;line-height:84px}
.welcome h2 span{color:var(--gold);display:block}
.welcome-copy{position:absolute;left:528px;top:68px;width:552px;font-size:13.6px;line-height:17.6px;color:var(--white)}
.welcome-copy p+p{margin-top:17px}

/* testimonial */
.testimonial{position:absolute;left:0;top:1319px;width:1200px;height:301px;background:var(--ink)}
.testimonial .rule{position:absolute;left:122px;top:90px;width:954px;height:1px;background:var(--line)}
.quote-mark{position:absolute;left:556px;top:44px}
.quote-text{position:absolute;left:0;top:134px;width:1200px;text-align:center;font-size:24px;font-weight:300;line-height:31px;color:#d6d6d6}
.quote-author{position:absolute;left:0;top:227px;width:1200px;text-align:center;font-size:15px;font-weight:700}
.quote-author span{color:var(--gold);margin-left:6px}
.dots{position:absolute;display:flex;gap:8px}
.dots i{width:10px;height:10px;border-radius:50%;background:var(--gold)}
.dots i.on{background:var(--accent-red)}

/* concerts */
.concerts{position:absolute;left:0;top:1620px;width:1200px;height:467px}
.concerts .strip{position:absolute;left:0;top:0;width:119px;height:467px;background:var(--sand)}
.schedule{position:absolute;left:119px;top:0;width:388px;height:467px;background:var(--ink)}
.schedule h2{position:absolute;left:0;top:10px;width:388px;text-align:center;font-weight:700;font-size:64px;line-height:56px}
.schedule h2 span{display:block;color:var(--gold)}
.next-bar{position:absolute;left:0;top:138px;width:388px;height:64px;background:var(--gold-deep);font-size:26px;font-weight:700;line-height:64px;padding-left:28px}
.calendar{position:absolute;left:328px;top:152px}
.event{position:absolute;left:32px;width:340px;font-weight:700}
.event .date{font-size:16px;color:var(--white)}
.event .place{font-size:19px;color:var(--gold);line-height:26px;margin-top:14px}
.event-rule{position:absolute;left:0;top:345px;width:376px;height:1px;background:var(--line)}
.map{position:absolute;left:507px;top:0;width:693px;height:467px;
  background:
   radial-gradient(ellipse 180px 120px at 330px 220px,#efe7dc 0%,transparent 70%),
   linear-gradient(135deg,#c9ae8a 0%,#b89670 45%,#d2bb99 100%)}
.pin{position:absolute;width:38px;height:48px;background:#2a2a2a;color:var(--white);text-align:center;font-weight:700;font-size:12px;line-height:13px;padding-top:4px}
.pin small{display:block;font-size:7px}

/* footer */
.site-footer{position:absolute;left:0;top:2087px;width:1200px;height:174px;background:var(--ink);text-align:center}
.footer-brand{position:absolute;left:0;top:30px;width:1200px;color:var(--gold);font-weight:700;line-height:1}
.footer-brand .brand-name{font-size:38px;letter-spacing:2px;display:block}
.footer-brand .brand-sub{font-size:10px;letter-spacing:2.4px;display:block;margin-top:5px}
.copyright{position:absolute;left:0;top:110px;width:1200px;font-size:12px;color:var(--white)}
.footer-links{position:absolute;left:0;top:137px;width:1200px;font-size:12px;color:var(--white)}
</style>
</head>
<body>

<section class="hero">
  <div class="hero-photo" role="img" aria-label="Concert photo: a young woman in headphones singing in front of a crowd with raised hands under stage lights"></div>
  <svg class="hero-arrow" width="22" height="30" viewBox="0 0 22 30"><path d="M5 3 L17 15 L5 27" fill="none" stroke="#ffffff" stroke-width="4"/></svg>

  <header class="site-header">
    <div class="brand"><span class="brand-name">VIREO</span><span class="brand-sub">MUSIC PRODUCTIONS</span></div>
    <div class="account-link">login / register</div>
    <div class="social" style="left:789px" aria-label="social link"></div>
    <div class="social" style="left:821px" aria-label="social link"></div>
    <div class="social" style="left:855px" aria-label="social link"></div>
    <div class="search"><svg width="30" height="30" viewBox="0 0 30 30"><circle cx="13" cy="13" r="6" fill="none" stroke="#fff" stroke-width="2"/><path d="M17.5 17.5 L22 22" stroke="#fff" stroke-width="2.4"/></svg></div>
    <nav class="main-nav">
      <a class="nav-about active">About <span>Vireo</span></a>
      <a class="nav-team">Team <span>Vireo</span></a>
      <a class="nav-join">Join <span>Vireo</span></a>
      <a>Contact <span>Vireo</span></a>
    </nav>
  </header>

  <div class="tagline-small">We turn aspiring musicians into</div>
  <div class="tagline-big">SuperStars!</div>

  <form class="signup">
    <h2><span class="h-small">GET FOUND AND</span><span class="h-big">BECOME A STAR!</span></h2>
    <div class="field" style="left:46px;top:136px;width:307px;height:30px">First name</div><span class="req" style="left:355px;top:130px">*</span>
    <div class="field" style="left:372px;top:136px;width:305px;height:30px">Last name</div><span class="req" style="left:680px;top:130px">*</span>
    <div class="field" style="left:46px;top:183px;width:141px;height:30px">Age</div>
    <div class="field" style="left:209px;top:183px;width:144px;height:30px">Zip Code</div>
    <div class="field" style="left:372px;top:183px;width:305px;height:30px">Email Address</div><span class="req" style="left:680px;top:177px">*</span>
    <div class="field" style="left:46px;top:226px;width:307px;height:30px">Daytime Phone</div>
    <div class="field" style="left:372px;top:226px;width:305px;height:30px">Evening Phone</div>
    <div class="field" style="left:46px;top:268px;width:631px;height:75px">Comments</div>
    <div class="artist-photo" role="img" aria-label="Black and white photo of a young rapper in a hood and headphones"></div>
    <div class="submit">SUBMIT</div>
    <p class="form-note">After submitting, you will have the opportunity to upload demos of your music (optional) and provide other pertinent information about yourself, band, or group.</p>
  </form>
</section>

<section class="welcome" role="img" aria-label="Warm-toned photo of a guitarist performing on a dim stage">
  <h2>Welcome <span>to Vireo</span></h2>
  <div class="welcome-copy">
    <p>Lorem ipsum dolor sit amet, consectetur adipiscing elit. Sed adipiscing sit amet sem sit amet viverra. Cras porta justo risus, quis sodales diam placerat vitae. Quisque eget dui orci. Cras aliquet, odio quis gravida fermentum, nibh lorem vulputate nunc, ut condimentum mauris ipsum non ipsum. Duis eleifend mauris nibh, ac hendrerit nisi bibendum dignissim. Nullam blandit urna vulputate nisl dignissim, vel tempus ante porttitor. Sed sed mi ac eros viverra rhoncus. Sed tempor sodales libero sit amet convallis.</p>
    <p>Morbi ac lectus lectus. Proin vitae facilisis enim. Suspendisse a fermentum magna. Curabitur accumsan ac magna ac vehicula. Sed sollicitudin, magna sed commodo pretium, arcu nunc tincidunt sem, quis laoreet felis eros et arcu. Maecenas porta tempus vulputate. Sed iaculis orci adipiscing lectus molestie dapibus. In vehicula, libero sit amet dapibus luctus, felis massa tincidunt eros, sodales fringilla lorem sem nec diam.</p>
  </div>
</section>

<section class="testimonial">
  <div class="rule"></div>
  <svg class="quote-mark" width="88" height="48" viewBox="0 0 88 48"><path d="M2 47 A42 42 0 0 1 86 47" fill="#0b0b0b" stroke="#5e5a50" stroke-width="1.5"/><text x="44" y="42" text-anchor="middle" font-family="Lato, sans-serif" font-weight="900" font-size="42" fill="#ffffff">&#8220;</text></svg>
  <p class="quote-text">" Lorem ipsum dolor sit amet, consectetur adipiscing elit. In imperdiet diam augue,<br>vitae lacinia leo lacinia sit amet. Nulla facilisi. Cras cursus sed odio a mollis"</p>
  <p class="quote-author">Mara Ellison <span>producers</span></p>
  <div class="dots" style="left:567px;top:276px"><i class="on"></i><i></i><i></i></div>
</section>

<section class="concerts">
  <div class="strip"></div>
  <div class="schedule">
    <h2>Concert <span>schedule</span></h2>
    <div class="next-bar">NEXT CONCERT</div>
    <svg class="calendar" width="38" height="36" viewBox="0 0 38 36"><rect x="1" y="5" width="36" height="30" fill="none" stroke="#fff" stroke-width="2"/><rect x="1" y="5" width="36" height="7" fill="#fff"/><rect x="8" y="1" width="3" height="8" fill="#fff"/><rect x="27" y="1" width="3" height="8" fill="#fff"/><g fill="#fff"><rect x="6" y="15" width="5" height="4"/><rect x="14" y="15" width="5" height="4"/><rect x="22" y="15" width="5" height="4"/><rect x="30" y="15" width="4" height="4"/><rect x="6" y="22" width="5" height="4"/><rect x="14" y="22" width="5" height="4"/><rect x="22" y="22" width="5" height="4"/><rect x="30" y="22" width="4" height="4"/><rect x="6" y="29" width="5" height="3"/><rect x="14" y="29" width="5" height="3"/></g></svg>
    <div class="dots" style="left:174px;top:218px"><i class="on"></i><i></i><i></i></div>
    <div class="event" style="top:244px"><div class="date">2 November 2013</div><div class="place">Harbor Hall - 2450 W Larkspur Ave,<br>Los Angeles, CA, US</div></div>
    <div class="event-rule"></div>
    <div class="event" style="top:366px"><div class="date">10 November 2013</div><div class="place">Harbor Hall - 2450 W Larkspur Ave,<br>Los Angeles, CA, US</div></div>
  </div>
  <div class="map" role="img" aria-label="Map of the south-western United States showing concert locations">
    <div class="pin" style="left:204px;top:84px">10<br>Nov<small>2013</small></div>
    <div class="pin" style="left:97px;top:166px">2<br>Nov<small>2013</small></div>
  </div>
</section>

<footer class="site-footer">
  <div class="footer-brand"><span class="brand-name">VIREO</span><span class="brand-sub">MUSIC PRODUCTIONS</span></div>
  <p class="copyright">Copyright 2013 © Music Producers.</p>
  <p class="footer-links">Privacy Policy | Terms and Conditions | Site Map | Feedback | Report Bug | Contact Us</p>
</footer>

</body>
</html>
```